Nutrition-Cooking Website

Hello!
I am in a need of a lovely looking website for my new nutrition practice. I am looking for something sleek, sophisticated, professional yet also welcoming.

Here is a current layout which can be tweaked or overhauled. I feel like the website is not quite what I want so thats why I need your help!!
http://tolvanfolio.example/RENATA-OSSLER-concept-15/

Two websites I like are: (layout similar to www.marquetta.example) or http://www.pernillavostraken.example

Here are the tabs for the website:
About Registered Dietitian Healthy Recipes Philanthropy Shop Features Contact Blog

Features for the Home page include:
Slideshow with 3 rotating updates (like www.marquetta.example)
Video Box (like www.marquetta.example)
Recent Recipes (like http://harrowfield7731.example)
Recent Posts (like http://harrowfield7731.example)
Food Knowledge Box- quick tidbits on laws on food (like www.marquetta.example- she has food wisdom)
Tried and True Benefits of Mediterranean Cuisine (like www.marquetta.example)
Picture of me with brief quote/bio (like www.bettinoruval.example)
Social media buttons

Color Scheme:
• I like the white with gold embroidery or the pretty bluish/purplish in the first pic would be awesome with the slight pink undertones (http://glossedtwirl.example/2012/10/quorvel-marigelle-collection-by-tansley/)
• Also like this goldish background- exotic/sophisticated- http://www.thewhirlingcook.example/Home.html
• Also like the rustic goldish look in the background like this-
ohttp://img.prentlo.example/vexomarks_rsvp_vintage_rustic_gold_swirls_invitation-p161658028764768924bebn6_400.jpg
o http://img.prentlo.example/vexomarks_ornamental_rustic_gold_swirls_invitation-p161776340110432961bvddb_400.jpg
• maybe can have the vines as grapes/olives
OPEN TO ALL DIFFERENT COLORS SCHEMES- whatever looks, clean, sophisticated and professional

Logo:
• Attached is the logo

Budget is flexible. If you think you can improve the website- please do so :)

Target Market(s)

health conscious individuals of all ages

Industry/Entity Type

Embroidery

Requirements
Must have
• clean and sharp look
professional looking
Should not have
• too much busyness

```html
<!DOCTYPE html>
<html lang="en">
<head>
<meta charset="utf-8">
<title>Renata Ossler RD</title>
<link rel="stylesheet" href="https://fonts.googleapis.com/css2?family=Cinzel:wght@400;700&family=Open+Sans:wght@400;600;700&display=swap">
<style>
:root{
  --page:#fbe9d5;
  --cream:#f7efdc;
  --cream-line:#e3d3b4;
  --nav:#efe1c2;
  --gold:#eeb04a;
  --gold-dark:#d69c2c;
  --brown:#5b3d20;
  --text:#5a4a3a;
  --muted:#8a7a6a;
  --red:#e0143c;
  --yellow:#f7c51c;
  --blue:#48b6e6;
  --pink:#e8174f;
  --olive:#d3a72a;
  --white:#fff;
}
*{box-sizing:border-box;margin:0;padding:0}
html,body{width:772px;height:1200px;overflow:hidden;background:var(--page)}
body{font-family:"Open Sans",Arial,sans-serif;color:var(--text)}
.canvas{position:relative;width:772px;height:1200px;overflow:hidden;
  background:repeating-linear-gradient(90deg,#fbe9d5 0 6px,#f8e4cf 6px 7px)}
.abs{position:absolute}
.serif{font-family:"Cinzel",Georgia,serif}

.brand{left:52px;top:40px;font-family:"Cinzel",Georgia,serif;font-size:27px;letter-spacing:2px;color:#3d2a1a}
.social{display:flex;gap:9px}
.social span{width:22px;height:22px;border-radius:50%;background:#c94a2c;display:block}
.social.top{left:505px;top:47px}
.social.bottom{left:505px;top:1151px}

.nav{left:41px;top:103px;width:671px;height:39px;background:var(--nav);border-top:3px dotted var(--gold-dark);border-bottom:3px dotted var(--gold-dark);display:flex;align-items:center;font-size:10.5px;color:#5a4024}
.nav a{text-decoration:none;color:inherit;padding:0 15px;height:100%;display:flex;align-items:center}
.nav a.active{background:var(--gold);color:#3a2810;padding:0 26px}

.frame{background:var(--cream);border:1px solid var(--cream-line)}
.slider{left:41px;top:153px;width:476px;height:230px}
.slide-photo{left:4px;top:4px;width:466px;height:221px;background:linear-gradient(135deg,#4c6a2a 0%,#9a7a3a 35%,#d8a050 55%,#b8432a 75%,#5a3a2a 100%)}
.slide-caption{left:4px;bottom:4px;width:466px;height:38px;background:rgba(40,25,10,.75);display:flex;align-items:center;padding:0 10px;justify-content:space-between}
.slide-caption h2{font-family:"Cinzel",Georgia,serif;color:#fff;font-weight:400;font-size:17px}
.btn{display:flex;align-items:center;justify-content:center;font-family:"Open Sans",Arial,sans-serif;font-weight:700;font-size:10px;border-radius:5px;color:#4a2e06}
.btn.know{width:78px;height:20px;background:linear-gradient(#ffd84a,#f0ac10)}
.arrow{width:20px;height:20px;background:#111;display:flex;align-items:center;justify-content:center}
.arrow.left{left:-1px;top:104px}
.arrow.right{left:455px;top:104px}

.bio{left:525px;top:153px;width:187px;height:230px;background:#fff;border:1px solid var(--cream-line)}
.bio-photo{left:8px;top:6px;width:171px;height:170px;background:linear-gradient(180deg,#fff 0%,#f1dccb 55%,#c96a3a 100%)}
.bio h3{left:0;top:183px;width:100%;text-align:center;font-family:"Cinzel",Georgia,serif;font-size:16px;color:#4a3320;font-weight:400}
.bio p{left:0;top:202px;width:100%;text-align:center;font-family:"Cinzel",Georgia,serif;font-size:9px;color:#4a3320;letter-spacing:1px}

.video-box{left:41px;top:396px;width:476px;height:180px}
.video-box h3{left:16px;top:16px;font-family:"Cinzel",Georgia,serif;font-size:14px;font-weight:700;color:#5b3d20}
.video-box p{left:16px;top:40px;width:188px;font-size:8.5px;line-height:12px;color:#6a5a4a}
.btn.videos{left:15px;top:101px;width:107px;height:28px;background:linear-gradient(#ffd84a,#f2b00e);font-size:10.5px;border-radius:4px}
.player{left:220px;top:4px;width:251px;height:172px;background:#000}
.player .replay{left:102px;top:66px;color:#eee;font-size:9px;display:flex;align-items:center;gap:4px}
.player .replay i{width:14px;height:10px;background:#777;border-radius:2px;display:block}
.controls{left:0;bottom:0;width:100%;height:12px;background:#d8d8d8;display:flex;align-items:center;gap:4px;padding:0 4px;font-size:6px;color:#333}
.controls .bar{flex:1;height:3px;background:#c81e1e}

.col{top:588px;height:491px}
.col h3{position:absolute;top:10px;left:0;width:100%;text-align:center;font-family:"Cinzel",Georgia,serif;font-size:13px;color:#5b3d20;font-weight:700}
.recipes{left:41px;width:239px}
.blogs{left:285px;width:229px}
.recipe{position:absolute;width:105px;height:138px;background:#fff;border:1px solid #e6dcc8}
.recipe .ph{margin:3px;height:100px}
.recipe p{font-size:8px;color:#8a7a6a;text-align:center;line-height:10px;padding:2px 6px}
.blog{position:absolute;left:0;width:217px;height:92px;border-bottom:1px solid #d8c8a8}
.blog .ph{position:absolute;left:12px;top:12px;width:54px;height:50px;border:2px solid #fff;background:linear-gradient(135deg,#f0b030,#c8202a 55%,#6a1020)}
.blog h4{position:absolute;left:76px;top:12px;font-size:8px;font-weight:400;color:#8a7a6a}
.blog .count{position:absolute;left:76px;top:23px;font-size:7px;color:var(--red)}
.blog .rule{position:absolute;left:76px;top:34px;width:132px;border-top:1px dotted #b8a888}
.blog p{position:absolute;left:76px;top:38px;width:134px;font-size:7px;line-height:10px;color:#6a5a4a}
.scroll{left:217px;top:2px;width:10px;height:487px;background:#eee;border-left:1px solid #ddd}
.scroll i{position:absolute;left:1px;top:14px;width:7px;height:100px;background:#fff;border:1px solid #ccc;border-radius:2px}

.widget{left:526px;width:187px;background:#fff;border:1px solid}
.widget .head{height:38px;display:flex;align-items:center;justify-content:center;font-family:"Cinzel",Georgia,serif;font-size:17px;color:#fff}
.widget .ph{margin:6px 6px 0;height:70px}
.widget h5{margin:9px 6px 0;font-size:9px;font-weight:600}
.widget p{margin:3px 6px 0;font-size:8px;line-height:11.5px;color:#444}
.widget .btn{margin:17px auto 0;width:107px;height:29px;font-size:10px}
.w-gold{top:396px;height:248px;border-color:var(--olive)}
.w-gold .head{background:var(--olive)}
.w-gold h5{color:#e59a10}
.w-gold .btn{background:linear-gradient(#f0c840,#c99a18)}
.w-blue{top:655px;height:248px;border-color:var(--blue)}
.w-blue .head{background:var(--blue)}
.w-blue h5{color:#e59a10}
.w-blue .btn{background:linear-gradient(#6ccaf2,#2e9ed6);color:#123a52}
.w-pink{top:913px;height:166px;border-color:var(--pink)}
.w-pink .head{background:var(--pink)}
.w-pink p{margin-top:9px}
.w-pink .btn{background:linear-gradient(#f43a6a,#c80c3a);color:#5a0418;margin-top:22px}

.newsletter{left:41px;top:1098px;width:671px;height:41px;background:var(--gold);border-top:3px dotted #c8861a;border-bottom:3px dotted #c8861a;display:flex;align-items:center;padding:0 8px}
.newsletter h4{font-family:"Cinzel",Georgia,serif;font-weight:400;font-size:15px;color:#fff}
.newsletter .field{margin-left:10px;width:187px;height:20px;background:#fff;border:1px solid #c89030;font-size:7.5px;color:#bbb;padding:5px}
.newsletter .signup{margin-left:8px;width:80px;height:20px;background:linear-gradient(#777,#4a4a4a);color:#222;font-weight:700;font-size:10px;display:flex;align-items:center;justify-content:center}
.footer-links{left:49px;top:1149px;font-size:7px;color:#7a6a5a}
.copyright{left:49px;top:1164px;font-size:7px;color:#7a6a5a}
</style>
</head>
<body>
<div class="canvas">
  <div class="abs brand">Renata Ossler RD</div>
  <div class="abs social top"><span></span><span></span><span></span><span></span><span></span><span></span><span></span></div>

  <nav class="abs nav">
    <a class="active">Home</a><a>About</a><a>Registered</a><a>Dietitian</a><a>Healthy Recipes</a><a>Philanthropy</a><a>Shop</a><a>Features</a><a>Blog</a><a>Contact</a>
  </nav>

  <section class="abs frame slider">
    <div class="abs slide-photo" role="img" aria-label="Vegetable pizza slice with salad leaves"></div>
    <div class="abs slide-caption"><h2>Secret Receipes for Vegetable Pizzas</h2><span class="btn know">KNOW MORE</span></div>
    <div class="abs arrow left"><svg width="8" height="10"><path d="M7 0 L1 5 L7 10Z" fill="#fff"/></svg></div>
    <div class="abs arrow right"><svg width="8" height="10"><path d="M1 0 L7 5 L1 10Z" fill="#fff"/></svg></div>
  </section>

  <section class="abs bio">
    <div class="abs bio-photo" role="img" aria-label="Portrait of Renata Ossler holding a sign"></div>
    <h3 class="abs">Renata Ossler</h3>
    <p class="abs">Bio, press &amp; More</p>
  </section>

  <section class="abs frame video-box">
    <h3 class="abs">Renata Latest Video</h3>
    <p class="abs">In interdum euismod ante, nec blandit nunc malesuada in. Nunc urna nulla, mollis at pellentesque vel, viverra eget velit. Suspendisse facilisis.</p>
    <span class="abs btn videos">MORE VIDEOS</span>
    <div class="abs player">
      <div class="abs replay"><i></i>Replay</div>
      <div class="abs controls">
        <svg width="6" height="7"><path d="M0 0 L6 3.5 L0 7Z" fill="#222"/></svg>
        <span>3:12 / 3:12</span><span class="bar"></span>
      </div>
    </div>
  </section>

  <section class="abs frame col recipes">
    <h3>Recent Recipies</h3>
    <div class="recipe" style="left:10px;top:40px"><div class="ph" role="img" aria-label="Cherry tomatoes in a bowl" style="background:linear-gradient(135deg,#f0a030,#c81e58)"></div><p>Lorem ipsum dolor sit amet</p></div>
    <div class="recipe" style="left:126px;top:40px"><div class="ph" role="img" aria-label="Fried chicken pieces" style="background:linear-gradient(135deg,#e0a050,#a4501a)"></div><p>Lorem ipsum dolor sit amet</p></div>
    <div class="recipe" style="left:10px;top:193px"><div class="ph" role="img" aria-label="Chocolate truffles" style="background:linear-gradient(135deg,#7a4a2a,#2a140a)"></div><p>Lorem ipsum dolor sit amet</p></div>
    <div class="recipe" style="left:126px;top:193px"><div class="ph" role="img" aria-label="Pasta with egg" style="background:linear-gradient(135deg,#c8502a,#e8b860)"></div><p>Lorem ipsum dolor sit amet</p></div>
    <div class="recipe" style="left:10px;top:343px"><div class="ph" role="img" aria-label="Grilled peppers" style="background:linear-gradient(135deg,#f08030,#c8301a)"></div><p>Lorem ipsum dolor sit amet</p></div>
    <div class="recipe" style="left:126px;top:343px"><div class="ph" role="img" aria-label="Fresh vegetables platter" style="background:linear-gradient(135deg,#5a8a2a,#c87a3a)"></div><p>Lorem ipsum dolor sit amet</p></div>
  </section>

  <section class="abs frame col blogs">
    <h3>Recent Blogs</h3>
    <div class="blog" style="top:24px"><div class="ph" role="img" aria-label="Blog thumbnail"></div><h4>Lorem ipsum dolor sit amet</h4><span class="count">1802 blogs</span><span class="rule"></span><p>Vestibulum ante ipsum primis in faucibus orci luctus et ultrices posuere cubilia Curae; Etiam urna justo,</p></div>
    <div class="blog" style="top:116px"><div class="ph" role="img" aria-label="Blog thumbnail"></div><h4>Lorem ipsum dolor sit amet</h4><span class="count">1802 blogs</span><span class="rule"></span><p>Vestibulum ante ipsum primis in faucibus orci luctus et ultrices posuere cubilia Curae; Etiam urna justo,</p></div>
    <div class="blog" style="top:208px"><div class="ph" role="img" aria-label="Blog thumbnail"></div><h4>Lorem ipsum dolor sit amet</h4><span class="count">1802 blogs</span><span class="rule"></span><p>Vestibulum ante ipsum primis in faucibus orci luctus et ultrices posuere cubilia Curae; Etiam urna justo,</p></div>
    <div class="blog" style="top:300px"><div class="ph" role="img" aria-label="Blog thumbnail"></div><h4>Lorem ipsum dolor sit amet</h4><span class="count">1802 blogs</span><span class="rule"></span><p>Vestibulum ante ipsum primis in faucibus orci luctus et ultrices posuere cubilia Curae; Etiam urna justo,</p></div>
    <div class="blog" style="top:392px;border-bottom:none"><div class="ph" role="img" aria-label="Blog thumbnail"></div><h4>Lorem ipsum dolor sit amet</h4><span class="count">1802 blogs</span><span class="rule"></span><p>Vestibulum ante ipsum primis in faucibus orci luctus et ultrices posuere cubilia Curae; Etiam urna justo,</p></div>
    <div class="abs scroll"><i></i></div>
  </section>

  <aside class="abs widget w-gold">
    <div class="head">Kirchen Witter</div>
    <div class="ph" role="img" aria-label="Grilled meat with vegetables" style="background:linear-gradient(135deg,#6a2a1a,#b8502a 50%,#3a1a10)"></div>
    <h5>Lorem ipsum dolor sit amet</h5>
    <p>In interdum euismod ante, nec bla ndit nunc malesuada in. Nunc urna nulla, mollis at pell ent esque vel, vive rra eget velit. Suspen disse facilisis, ante a tincidunt faucibus, orci sem porta erat.</p>
    <span class="btn">READ MORE</span>
  </aside>

  <aside class="abs widget w-blue">
    <div class="head">Kirchen Witter</div>
    <div class="ph" role="img" aria-label="Cream pastries" style="background:linear-gradient(135deg,#c89a6a,#f0e0c0 50%,#8a6a4a)"></div>
    <h5>Lorem ipsum dolor sit amet</h5>
    <p>In interdum euismod ante, nec bla ndit nunc malesuada in. Nunc urna nulla, mollis at pell ent esque vel, vive rra eget velit. Suspen disse facilisis, ante a tincidunt faucibus, orci sem porta erat.</p>
    <span class="btn">READ MORE</span>
  </aside>

  <aside class="abs widget w-pink">
    <div class="head">Kitchen Wisdom</div>
    <p>In interdum euismod ante, nec bla ndit nunc malesuada in. Nunc urna nulla, mollis at pell ent esque vel, vive rra eget velit. Suspen disse facilisis, ante a tincidunt faucibus, orci sem porta erat.</p>
    <span class="btn">READ MORE</span>
  </aside>

  <section class="abs newsletter">
    <h4>Join the Renata Monthly Newsletter</h4>
    <div class="field">EMAIL ADDRESS</div>
    <div class="signup">SIGN UP</div>
  </section>

  <div class="abs footer-links">privacy Policy &nbsp;|&nbsp; Terms &amp; Conditions &nbsp;|&nbsp; Sitemap</div>
  <div class="abs copyright">© 2013, All Rights Reserved, RenataOssler Rd.com</div>
  <div class="abs social bottom"><span></span><span></span><span></span><span></span><span></span><span></span><span></span></div>
</div>
</body>
</html>
```